Lark Stewardship Business Card design

We need a creative business card design for our hospitality management company
We need the following information:
Our business Logo: Lark Stewardship
Name: Mira Dalvorsen
Phone number: 0468 319 542
Email: mira@larkstewardship.com.au
Address: 214/53 Pemberly Street, South Kelbrook 3218
Web: www.larkstewardship.com.au
I need the design to be a working file so that I can insert the names and numbers of the other staff members of our business.
The cards need to be 90 x 40mm
Thanks
Hospitality

```html
<!DOCTYPE html>
<html lang="en">
<head>
<meta charset="utf-8">
<title>Lark Stewardship Business Card</title>
<link rel="stylesheet" href="https://fonts.googleapis.com/css2?family=Barlow:wght@400;500&family=Barlow+Condensed:wght@700&display=swap">
<style>
  :root {
    --stage: #dcdcda;
    --card-top: #14507c;
    --card-mid: #0f3c62;
    --card-deep: #081626;
    --accent: #3ea0dc;
    --glow: #1d8fd6;
    --ink-white: #ffffff;
    --ink-soft: #dbe6ef;
    --mark-dark: #0a1622;
  }
  * { margin: 0; padding: 0; box-sizing: border-box; }
  html, body { width: 1200px; height: 534px; overflow: hidden; }
  body {
    background: var(--stage);
    position: relative;
    font-family: "Barlow", Arial, sans-serif;
  }
  .card {
    position: absolute;
    top: 151px;
    width: 517px;
    height: 229px;
    overflow: hidden;
    background: linear-gradient(180deg, var(--card-top) 0%, var(--card-mid) 55%, var(--card-deep) 100%);
  }
  .card--front { left: 62px; }
  .card--back { left: 622px; }

  .front-sheen {
    position: absolute; inset: 0;
    background: linear-gradient(120deg, rgba(90,170,230,0.55) 0%, rgba(60,140,210,0.35) 40%, rgba(0,0,0,0) 40.2%);
  }
  .front-block {
    position: absolute;
    left: 26px; top: 8px;
    width: 190px; height: 213px;
    background: #05080c;
    box-shadow: 0 0 0 3px var(--glow), 0 0 14px rgba(29,143,214,0.7);
  }

  .brand {
    position: absolute;
    left: 258px; top: 32px;
    display: flex; align-items: center; gap: 9px;
  }
  .brand__square {
    width: 38px; height: 38px;
    background: var(--ink-white);
  }
  .brand__name {
    font-family: "Barlow Condensed", "Arial Narrow", sans-serif;
    font-weight: 700;
    font-size: 17px;
    color: var(--ink-white);
    text-transform: uppercase;
    letter-spacing: 0.2px;
  }

  .contact {
    position: absolute;
    left: 258px; top: 100px;
    color: var(--ink-soft);
  }
  .contact__name {
    font-size: 15px;
    font-weight: 500;
    color: var(--accent);
    text-transform: uppercase;
    letter-spacing: 0.3px;
    margin-bottom: 12px;
  }
  .contact__address {
    font-size: 11.5px;
    line-height: 15px;
    margin-bottom: 8px;
  }
  .contact__list { list-style: none; font-size: 11.5px; line-height: 13.5px; }
  .contact__list li { display: flex; align-items: center; gap: 6px; }
  .contact__list svg { width: 10px; height: 10px; fill: none; stroke: var(--ink-soft); stroke-width: 1.2; }

  .back-mark {
    position: absolute;
    left: 50%; top: 39px;
    width: 101px; height: 101px;
    transform: translateX(-50%);
    background: var(--mark-dark);
  }
  .back-name {
    position: absolute;
    left: 0; right: 0; top: 151px;
    text-align: center;
    font-family: "Barlow Condensed", "Arial Narrow", sans-serif;
    font-weight: 700;
    font-size: 38px;
    letter-spacing: 2.4px;
    color: var(--mark-dark);
    text-transform: uppercase;
  }
</style>
</head>
<body>
  <section class="card card--front">
    <div class="front-sheen"></div>
    <div class="front-block" role="img" aria-label="Large brand symbol area"></div>
    <div class="brand">
      <span class="brand__square"></span>
      <span class="brand__name">Lark Stewardship</span>
    </div>
    <div class="contact">
      <p class="contact__name">Mira Dalvorsen</p>
      <p class="contact__address">214/53 Pemberly Street,<br>South Kelbrook 3218</p>
      <ul class="contact__list">
        <li><svg viewBox="0 0 10 10"><path d="M2 1 L4 1 L4.5 3 L3.3 4 Q4.5 6 6 6.7 L7 5.5 L9 6 L9 8 Q5 9 1.5 4 Q1 2 2 1 Z" fill="#dbe6ef" stroke="none"/></svg>0468 319 542</li>
        <li><svg viewBox="0 0 10 10"><rect x="0.8" y="2" width="8.4" height="6"/><path d="M0.8 2 L5 5.5 L9.2 2"/></svg>mira@larkstewardship.com.au</li>
        <li><svg viewBox="0 0 10 10"><circle cx="5" cy="5" r="4"/><ellipse cx="5" cy="5" rx="1.8" ry="4"/><path d="M1 5 H9"/></svg>www.larkstewardship.com.au</li>
      </ul>
    </div>
  </section>

  <section class="card card--back">
    <div class="back-mark"></div>
    <p class="back-name">Lark Stewardship</p>
  </section>
</body>
</html>
```